Thai Menu Design Project

We need a new menu design for a Thai restaurant in Fort Worth, Texas. We are a family-owned and really proud about our food and our service. We want the menu to feel healthy, modern, delicious, artistic Thai, and friendly. The colors we used in our restaurant are maroon, burgundy, black, white, gold and pale yellow.

Please look at our website www.brindlewokery.com
for the reference of the menus and the photos we use.

The menu can be in any number of pages (the fewer the better though) The size of the paper is US letter.
Updates

Update:

- We don't put the photos of the food in the menu pages anymore, instead, we like to put the photos of the herbs and their benefits (found in the file 'herb benefits') on the menu pages instead.

- the paper size is US letter.

- we don't have specific numbers of pages but the fewer the better

Thank you!

I added logos and background photo again in case the previous files did not work. Thanks!

Target Market(s)

Trendy socialized people from 20-30s,couples of all ages from 20s-60s,and families.

Industry/Entity Type

Restaurant

Requirements
Must have
• We want the menu to feel healthy, modern, delicious, artistic, Thai, and friendly.

We like to keep the colors maroon, burgundy, black, gold, pale yellow, and off white.

We like to put the photos of the herbs and their benefits (available in the file called 'herb benefits') randomly in the menu pages.

*Please use the photos available in the file called 'herb benefits' along with its details somewhere in the pages. You can change the photo of each herb to the ones you find more fitting from the internet.

Nice to have
• If we can add the wallpaper pattern in our menu it will be great. It can be used in anyway.

```html
<!DOCTYPE html>
<html lang="en">
<head>
<meta charset="utf-8">
<title>Brindle Wokery – Menu Pages 2 and 3</title>
<link rel="stylesheet" href="https://fonts.googleapis.com/css2?family=Playfair+Display:ital,wght@1,700&family=Ubuntu:wght@400;500&family=Open+Sans:ital,wght@1,400&display=swap">
<style>
:root{
  --stage-light:#eceded;
  --stage-dark:#c9cacc;
  --label:#ffffff;
  --plum:#6a2356;
  --gold:#c9a250;
  --gold-deep:#a98335;
  --paper:#f4f0f1;
  --maroon:#7c1d2c;
  --ink:#3a2a30;
  --chili:#c0282d;
  --lime:#6aa43a;
}
*{box-sizing:border-box;margin:0;padding:0}
html,body{width:1200px;height:792px;overflow:hidden}
body{
  position:relative;
  background:radial-gradient(ellipse at 50% 40%,var(--stage-light) 0%,var(--stage-dark) 100%);
  font-family:"Ubuntu",sans-serif;color:var(--ink);
}
.page-label{position:absolute;top:32px;font:italic 24px "Open Sans",sans-serif;color:var(--label)}
.menu-page{position:absolute;top:85px;height:670px;background:var(--plum)}
.page-left{left:37px;width:490px}
.page-right{left:646px;width:519px}
.border-pattern{
  position:absolute;left:0;right:0;bottom:0;height:140px;
  background:linear-gradient(to bottom,var(--plum) 0%,#7d4a4a 60%,#a07a44 100%);
}
.panel{
  position:absolute;left:23px;top:23px;right:13px;bottom:20px;
  background:var(--paper);border:2px solid var(--gold);
}
.page-right .panel{right:24px}
.brand{
  position:absolute;left:0;right:0;top:27px;text-align:center;
  font:500 20px/24px "Ubuntu",sans-serif;color:var(--plum);
}
.brand::before{
  content:"";display:inline-block;width:9px;height:9px;border-radius:50%;
  background:var(--plum);margin-right:7px;vertical-align:2px;
}
.section-title{
  font:italic 700 25px/36px "Playfair Display",serif;color:var(--maroon);
  margin-bottom:12px;white-space:nowrap;
}
.column{position:absolute;top:88px;width:198px}
.item{margin-bottom:11px}
.soups .item{margin-bottom:9px}
.item-head{
  display:flex;align-items:baseline;white-space:nowrap;
  font-size:11px;line-height:14px;color:var(--maroon);
}
.item-head .leader{flex:1;border-bottom:1.5px dotted var(--maroon);margin:0 2px;transform:translateY(-3px)}
.item-head .small{font-size:8px}
.item-desc{font-size:8px;line-height:10px;color:var(--ink)}
.item-note{font-size:7.5px;line-height:11px;color:var(--maroon)}
.variant{display:flex;white-space:nowrap;font-size:7.5px;line-height:12px;color:var(--maroon)}
.variant .leader{flex:1;border-bottom:1px dotted var(--maroon);margin:0 2px;transform:translateY(-3px)}
.new-badge{
  display:inline-block;width:17px;height:9px;border-radius:5px;flex:none;
  background:linear-gradient(var(--gold),var(--gold-deep));margin-left:4px;align-self:center;
}
.spicy{
  display:inline-block;width:3px;height:8px;background:var(--chili);flex:none;
  border-radius:2px 2px 2px 0;transform:skewX(-15deg);margin-left:3px;align-self:flex-start;margin-top:1px;
}
.herb-card{
  position:absolute;left:253px;top:452px;width:192px;height:155px;overflow:hidden;
  background:var(--gold-deep);padding:6px 7px;color:#fff;
}
.herb-card h3{font:500 12px/15px "Ubuntu",sans-serif;letter-spacing:.5px;margin-bottom:2px}
.herb-card p{font-size:6px;line-height:8.6px}
.herb-card .lead{width:105px}
.herb-photo{
  position:absolute;right:2px;top:0;width:72px;height:54px;border-radius:27px;
  background:radial-gradient(circle at 40% 45%,#b9dc7a 0%,var(--lime) 45%,#3f7420 100%);
}
.divider{position:absolute;left:236px;top:90px;width:1px;height:530px;background:#bfa9b0}
.footnote{
  position:absolute;left:20px;top:552px;width:198px;height:56px;
  border:1.5px solid var(--maroon);border-radius:4px;background:#fff;
  font-size:8px;color:var(--maroon);text-align:center;line-height:11px;padding-top:5px;
}
.footnote .spicy{margin:0 3px 0 0;vertical-align:1px}
</style>
</head>
<body>

<div class="page-label" style="left:258px">Page 2</div>
<div class="page-label" style="left:867px">Page 3</div>

<section class="menu-page page-left">
  <div class="border-pattern" role="img" aria-label="Gold Thai ornamental pattern along the lower border"></div>
  <div class="panel">
    <div class="brand">Brindle Wokery</div>

    <div class="column" style="left:18px">
      <h2 class="section-title">Appetizers</h2>
      <div class="item"><div class="item-head">Chicken Satay (6)<span class="leader"></span>9</div><div class="item-desc">Marinated chicken on skewers served with our famous peanut sauce and cucumber salad</div></div>
      <div class="item"><div class="item-head">Coconut Shrimp (6)<span class="new-badge"></span><span class="leader"></span>8</div><div class="item-desc">Served with sweet spicy dipping sauce</div></div>
      <div class="item"><div class="item-head">Brindle Sampler<span class="leader"></span>14</div><div class="item-desc">2 Chicken Satay, 2 Golden Shrimp, 2 Pot Stickers, 2 Crab Rangoon, and 2 Crispy Spring Roll</div></div>
      <div class="item"><div class="item-head">Three Musketeers (V)<span class="new-badge"></span><span class="leader"></span>9</div><div class="item-desc">2 Awesome Taro, 2 Sweet Corn Cakes, and 2 Crispy Tofu. All Vegetarians!</div></div>
      <div class="item"><div class="item-head">Fried Calamari<span class="leader"></span>8</div><div class="item-desc">Battered calamari served with plum sauce</div></div>
      <div class="item"><div class="item-head">Crab Rangoon (6)<span class="leader"></span>7.5</div><div class="item-desc">Crab with cream cheese in crispy wonton skin</div></div>
      <div class="item"><div class="item-head">Fish Cake (6)<span class="new-badge"></span><span class="leader"></span>8</div><div class="item-desc">Thai-style spicy fishcake served with cucumber vinaigrette</div></div>
      <div class="item"><div class="item-head">Thai Beef Jerky<span class="leader"></span>9</div><div class="item-desc">Sliced fried beef marinated with Thai seasoning, served with flavorful dipping sauce</div></div>
      <div class="item"><div class="item-head">Sweet Corn cake (5) (V)<span class="leader"></span>7.5</div><div class="item-desc">Seasoned sweet corn battered and deep-fried served with sweet sauce</div></div>
      <div class="item"><div class="item-head">Chicken or Tofu Lettuce Wrap (V)<span class="leader"></span>9</div><div class="item-desc">Minced chicken or tofu, water chestnuts, mushrooms, scallions, crispy noodles and cool lettuce cups with spicy lime sauce</div></div>
      <div class="item"><div class="item-head">Crispy Soft Shell Crabs (2)<span class="leader"></span>8</div><div class="item-desc">Soft shell crabs fried to a light crisp served with sweet and spicy sauce</div></div>
    </div>

    <div class="column" style="left:250px;top:132px;width:200px">
      <div class="item"><div class="item-head">Pot Stickers (8)<span class="leader"></span>7.5</div><div class="item-desc">Pork and cabbage dumplings served steamed or fried</div></div>
      <div class="item"><div class="item-head">Mixed Vegetable Tempura (V)<span class="leader"></span>9</div><div class="item-desc">Breaded green beans, eggplant, carrot and broccoli served with Thai ginger sauce</div></div>
      <div class="item"><div class="item-head">Cucumber Salad (V)<span class="leader"></span>5</div><div class="item-desc">Sliced cucumber in sweet vinaigrette</div></div>
      <div class="item"><div class="item-head">Edamame (V)<span class="leader"></span>5</div><div class="item-desc">Steamed salted soybeans</div></div>
      <div class="item"><div class="item-head">Crispy Spring Rolls (5)<span class="leader"></span>7.50</div><div class="item-desc">Pork, carrot, cabbage, and noodles in Thai spring roll wrapper</div><div class="item-note">Vegetarian Spring Rolls (5) (V)</div></div>
      <div class="item"><div class="item-head">Egg Roll (1)<span class="leader"></span>1.65</div><div class="item-desc">Crispy eggroll stuffed with seasoned pork and cabbage</div><div class="item-note">Vegetarian Egg Roll (V)</div></div>
      <div class="item"><div class="item-head">Summer Rolls (2) (V)<span class="leader"></span>3</div><div class="item-desc">Romaine lettuce, vermicelli, cilantro, carrot, and red cabbage in rice wrapper served with peanut sauce. For Tofu or Shrimp add 1</div></div>
    </div>

    <aside class="herb-card">
      <div class="herb-photo" role="img" aria-label="Photo of whole and halved limes"></div>
      <h3>LIME</h3>
      <p class="lead">The first fruit that comes to mind when it comes to medicinal uses is perhaps the good old lime. The lime is the sweeter cousin of the lemon.</p>
      <p>Limes are packed with vitamin C. Fresh or from concentrate, lime juice contains more citric acid than orange or grapefruit juice. Limes are good for women's health. These citrus gems contain calcium and folate, two nutrients that are important for post-menopausal women and women of child-bearing age. Limes are anti-carcinogenic. The limonoid compounds in limes have been shown to prevent cancers of the colon, stomach and blood. Lime juice can help prevent formation of kidney stones.</p>
    </aside>
  </div>
</section>

<section class="menu-page page-right">
  <div class="border-pattern" role="img" aria-label="Gold Thai ornamental pattern along the lower border"></div>
  <div class="panel">
    <div class="brand">Brindle Wokery</div>

    <div class="column soups" style="left:18px">
      <h2 class="section-title">Soups</h2>
      <div class="item"><div class="item-head">Classic Tom Yum<span class="spicy"></span></div><div class="item-desc">Spicy lemongrass soup with mushroom, cilantro, lime juice &amp; chili.</div>
        <div class="variant">With Shrimp<span class="leader"></span>Bowl: 7 ... Hot Pot: 13.5</div>
        <div class="variant">or Mixed Vegetables</div>
        <div class="variant">With mixed Seafood<span class="leader"></span>Bowl: 8 ... Hot Pot: 15.5</div></div>
      <div class="item"><div class="item-head">Tom Yum Brindle<span class="spicy"></span></div><div class="item-desc">Classic Tom Yum with coconut milk for a smooth taste.</div>
        <div class="variant">With Shrimp<span class="leader"></span>Bowl: 7 ... Hot Pot: 13.5</div>
        <div class="variant">or Mixed Vegetables</div>
        <div class="variant">With mixed Seafood<span class="leader"></span>Bowl: 8 ... Hot Pot: 15.5</div></div>
      <div class="item"><div class="item-head">Seafood Poh Taek<span class="new-badge"></span><span class="leader"></span><span class="small">Hot Pot:&nbsp;</span>15.5</div><div class="item-desc">The full flavor of Thai super herbs, hot and tangy yet light and refreshing. Healthy and delicious.</div></div>
      <div class="item"><div class="item-head">Tom Kha</div><div class="item-desc">Galangal coconut soup with mushroom, cilantro, chili, and lime juice.</div>
        <div class="variant">With Chicken, Mixed<span class="leader"></span>Bowl: 7 ... Hot Pot: 13.5</div>
        <div class="variant">Vegetables, or Soft Tofu</div></div>
      <div class="item"><div class="item-head">Tom Sab E-Sarn<span class="spicy"></span></div><div class="item-desc">North-Eastern spicy &amp; sour soup flavored with herbs.</div>
        <div class="variant">Choice of Pork, Chicken ,<span class="leader"></span>Bowl: 6 ... Hot Pot: 11.5</div>
        <div class="variant">or Mixed Vegetables</div></div>
      <div class="item"><div class="item-head">Vegetable Tofu Soup (V)<span class="small">&nbsp;.. Bowl: 5 .. Hot Pot:&nbsp;</span>9.5</div><div class="item-desc">Thai style mild broth with mixed vegetable and soft tofu. Soup for the soul</div></div>
      <div class="item"><div class="item-head">Wanton Soup<span class="new-badge"></span><span class="small">&nbsp;.. Bowl: 5 ...... Hot Pot:&nbsp;</span>9.5</div></div>
    </div>

    <div class="divider"></div>

    <div class="column" style="left:251px;width:200px">
      <h2 class="section-title">Salads and Yum</h2>
      <div class="item"><div class="item-head">Larb<span class="spicy"></span><span class="leader"></span>10</div><div class="item-desc">North-Eastern spicy salad seasoned with herbs, shallots, scallions, roasted ground rice in spicy lime juice. Choice of chicken, pork, or soft tofu</div></div>
      <div class="item"><div class="item-head">Duck Salad<span class="new-badge"></span><span class="leader"></span>12</div><div class="item-desc">Marinated duck with tomatoes, onions, cilantro tossed with lime juice and Thai chili</div></div>
      <div class="item"><div class="item-head">Yum Woon Sen<span class="spicy"></span><span class="leader"></span>10</div><div class="item-desc">Spicy glass noodles with shrimp, ground pork, onions, cilantro, tomatoes in lime juice and chili</div></div>
      <div class="item"><div class="item-head">Som Tum (V)<span class="spicy"></span><span class="leader"></span>9</div><div class="item-desc">Papaya salad with Thai long green beans, tomatoes, and peanuts in spicy homemade dressing</div></div>
      <div class="item"><div class="item-head">Yum Neu<span class="spicy"></span><span class="leader"></span>10</div><div class="item-desc">Marinated grilled beef with tomatoes, onions, cilantro tossed with lime juice and Thai chili</div></div>
      <div class="item"><div class="item-head">Pla Goong<span class="spicy"></span><span class="leader"></span>11</div><div class="item-desc">Shrimp with cucumbers, tomatoes, onions, and cilantro tossed with lime juice and Thai chili</div></div>
      <div class="item"><div class="item-head">Spicy Seafood Salad<span class="spicy"></span><span class="leader"></span>12</div><div class="item-desc">Mixed seafood with sliced cucumber, tomatoes, onions, cilantro tossed with lime juice and Thai chili</div></div>
      <div class="item"><div class="item-head">House Salad<span class="leader"></span>7</div><div class="item-desc">Lettuce, onions, tomatoes &amp; sliced hard-boiled eggs with choice of Thai lime dressing or Thai peanut dressing</div>
        <div class="variant">With Grilled Chicken<span class="leader"></span><span style="font-size:10px">8.50</span></div>
        <div class="variant">With Grilled Shrimp<span class="leader"></span><span style="font-size:10px">9.50</span></div></div>
      <div class="item"><div class="item-head">Nam Sod<span class="leader"></span>10</div><div class="item-desc">Ground pork with lime juice, ginger, peanuts, onions and cilantro</div></div>
    </div>

    <div class="footnote"><span class="spicy"></span>For spicy dishes, please choose<br>spicy level from 1 to 5.<br>(V) for Vegetarian.<br>Up to 5 credit cards per check please.</div>
  </div>
</section>

</body>
</html>
```